Fashion Design Business Card

I need a new business card designed for a new fashion company. I have attached what I have currently designed. I want it more feminine looking, the logo needs to be gold. I want it simple, feminine and stylish. Please give me some different ideas with the fonts.
Updates

I need to send the design we currently have, as we have worked out the logo.
You also need all of our details
Industry/Entity Type
Fashion
Look and feel
Each slider illustrates characteristics of the customer's brand and the style your logo design should communicate.

```html
<!DOCTYPE html>
<html lang="en">
<head>
<meta charset="utf-8">
<title>Marlena Hart – Business Card</title>
<link rel="stylesheet" href="https://fonts.googleapis.com/css2?family=Cormorant+Garamond:ital,wght@0,400;0,500;1,400&family=Montserrat:wght@300;400&display=swap">
<style>
  :root {
    --page-bg: #ffffff;
    --card-coral: #f15a2b;
    --stitch-cream: #fff4ea;
    --text-white: #ffffff;
    --accent-gold: #f9c45a;
    --mark-gold: #f6cd5e;
  }
  * { margin: 0; padding: 0; box-sizing: border-box; }
  html, body {
    width: 1200px;
    height: 900px;
    overflow: hidden;
    background: var(--page-bg);
  }
  .canvas {
    position: relative;
    width: 1200px;
    height: 900px;
  }
  .card-shape {
    position: absolute;
    left: 0;
    top: 0;
  }
  .brand-mark {
    position: absolute;
    left: 150px;
    top: 318px;
    width: 320px;
    display: flex;
    flex-direction: column;
    align-items: center;
    gap: 22px;
  }
  .brand-ring {
    width: 150px;
    height: 150px;
    border-radius: 50%;
    border: 4px solid var(--mark-gold);
  }
  .brand-name {
    color: var(--mark-gold);
    font-family: "Cormorant Garamond", Georgia, serif;
    font-weight: 500;
    font-size: 44px;
    line-height: 1;
    letter-spacing: 1px;
    white-space: nowrap;
  }
  .identity {
    position: absolute;
    right: 156px;
    top: 378px;
    text-align: right;
  }
  .identity-name {
    color: var(--text-white);
    font-family: "Cormorant Garamond", Georgia, serif;
    font-style: italic;
    font-weight: 400;
    font-size: 64px;
    line-height: 1;
    letter-spacing: 0.5px;
  }
  .identity-role {
    margin-top: 12px;
    color: var(--accent-gold);
    font-family: "Montserrat", Arial, sans-serif;
    font-weight: 300;
    font-size: 24px;
    line-height: 1;
    letter-spacing: 6px;
    text-transform: lowercase;
  }
  .contact-list {
    position: absolute;
    right: 156px;
    top: 606px;
    list-style: none;
    text-align: right;
    color: var(--text-white);
    font-family: "Montserrat", Arial, sans-serif;
    font-weight: 300;
    font-size: 23px;
    line-height: 42px;
    letter-spacing: 0.3px;
  }
  .contact-label {
    margin-right: 10px;
    color: var(--accent-gold);
  }
</style>
</head>
<body>
  <main class="canvas">
    <svg class="card-shape" width="1200" height="900" viewBox="0 0 1200 900" aria-hidden="true">
      <path d="M80,132 H1010 A120,120 0 0 1 1130,252 V772 H80 Z" fill="var(--card-coral)"/>
      <path d="M96,148 H1010 A104,104 0 0 1 1114,252 V756 H96 Z" fill="none"
            stroke="var(--stitch-cream)" stroke-width="2" stroke-dasharray="7 5"/>
    </svg>

    <div class="brand-mark">
      <span class="brand-ring" aria-hidden="true"></span>
      <span class="brand-name">Marlena Hart</span>
    </div>

    <header class="identity">
      <h1 class="identity-name">Marlena Hart</h1>
      <p class="identity-role">fashion designer</p>
    </header>

    <ul class="contact-list">
      <li><span class="contact-label">ph.</span>0400512736</li>
      <li><span class="contact-label">email:</span>marlena@marlenahart.com</li>
      <li><span class="contact-label">web:</span>www.marlenahart.com</li>
    </ul>
  </main>
</body>
</html>
```